Brennock Metal recycling, a business card/logo for our industrial family metal recycling company

A new business card design/logo for our long established family metal recycling company.
I have a logo for our property company which was designed a few months ago on pixel forum which I would like to be very close to this design but have a more industrial feel to it and in a darker blue colour, please see attachments.

Target Market(s)

industries that produce metal waste for recycling, construction sites, engineering companies, manufactures, builders, plumbers, electricians, general house holders.

Industry/Entity Type

Recycling

Contact Information for Business Card

owner/director...Gordon brennock
e-mail....info@brennockscrapworks.example.co.uk
web address.....brennockscrapworks.example.co.uk

Font styles to use
Serif
Sans Serif

Colors
0255a3
ffffff

Requirements
Must have
• -dark blue business card on front.
-white on the back, see contact details, e-mail address for metal company.
-to have an industrial feel to it.
-brennock logo as business card attached but (brennock metal recycling)
please remove the little roof/arrow above brennock as this was relevant to property company.
Nice to have
• please see our website brennockscrapworks.example.co.uk with all details
being correct however I would like to refresh the logo to more like the brennock property investment business card logo attached.
Should not have
• should not contain details from property investments card as this design is for the metal recycling company.

```html
<!DOCTYPE html>
<html lang="en">
<head>
<meta charset="utf-8">
<title>Brennock Metal Recycling – Business Card</title>
<link rel="stylesheet" href="https://fonts.googleapis.com/css2?family=Raleway:wght@400;500;700&display=swap">
<style>
  :root {
    --brand-blue: #025a99;
    --brand-navy: #001e4d;
    --card-white: #fdfbfc;
    --backdrop: #b2c1d4;
    --ink-white: #ffffff;
  }
  * { margin: 0; padding: 0; box-sizing: border-box; }
  html, body {
    width: 1200px; height: 1200px; overflow: hidden;
    background: var(--backdrop);
    font-family: "Raleway", sans-serif;
  }
  .card {
    position: absolute; left: 285px; width: 630px; height: 360px; overflow: hidden;
  }
  .card--contact { top: 150px; background: var(--card-white); }
  .card--brand { top: 604px; background: var(--brand-blue); }

  .wordmark {
    position: absolute; font-family: "Raleway", sans-serif; font-weight: 400;
    line-height: 1; white-space: nowrap;
  }
  .wordmark__name { display: block; letter-spacing: 0.04em; }
  .wordmark__tagline { display: block; text-transform: uppercase; letter-spacing: 0.62em; }

  .card--contact .wordmark {
    right: 23px; top: 66px; color: var(--brand-blue); text-align: right;
  }
  .card--contact .wordmark__name { font-size: 58px; }
  .card--contact .wordmark__tagline { font-size: 11px; margin-top: 8px; margin-right: -6px; }

  .card--brand .wordmark {
    left: 0; right: 0; top: 128px; color: var(--ink-white); text-align: center;
  }
  .card--brand .wordmark__name { font-size: 84px; }
  .card--brand .wordmark__tagline { font-size: 16px; margin-top: 10px; margin-right: -10px; }

  .accent-band {
    position: absolute; left: 0; top: 180px; width: 425px; height: 48px;
    background: var(--brand-blue);
  }
  .contact-icons { position: absolute; top: 180px; left: 503px; height: 48px; display: flex; }
  .contact-icons__item {
    height: 48px; display: flex; align-items: center; justify-content: center;
    color: var(--ink-white);
  }
  .contact-icons__item--web { width: 50px; background: var(--brand-navy); }
  .contact-icons__item--mail { width: 54px; background: var(--brand-blue); font-size: 24px; }

  .person { position: absolute; left: 26px; top: 264px; color: var(--brand-blue); }
  .person__name { font-size: 22px; font-weight: 700; letter-spacing: 0.07em; line-height: 1.1; }
  .person__role { font-size: 16px; font-weight: 400; letter-spacing: 0.06em; margin-top: 3px; }

  .contact-lines {
    position: absolute; right: 24px; top: 264px; text-align: right;
    color: var(--brand-blue); font-size: 16px; letter-spacing: 0.05em; line-height: 22px;
  }
</style>
</head>
<body>
  <section class="card card--contact" aria-label="Business card, contact side">
    <div class="wordmark">
      <span class="wordmark__name">brennock</span>
      <span class="wordmark__tagline">Metal Recycling</span>
    </div>

    <div class="accent-band"></div>

    <div class="contact-icons">
      <div class="contact-icons__item contact-icons__item--web" aria-label="Website">
        <svg width="22" height="22" viewBox="0 0 22 22" fill="none" stroke="#fff" stroke-width="1.4">
          <circle cx="11" cy="11" r="9.5"/>
          <ellipse cx="11" cy="11" rx="4.2" ry="9.5"/>
          <line x1="11" y1="1.5" x2="11" y2="20.5"/>
          <line x1="1.5" y1="11" x2="20.5" y2="11"/>
          <line x1="3" y1="6.5" x2="19" y2="6.5"/>
          <line x1="3" y1="15.5" x2="19" y2="15.5"/>
        </svg>
      </div>
      <div class="contact-icons__item contact-icons__item--mail" aria-label="Email">@</div>
    </div>

    <div class="person">
      <p class="person__name">Gordon Brennock</p>
      <p class="person__role">Owner-Director</p>
    </div>

    <div class="contact-lines">
      <p>info@brennockscrapworks.example.co.uk</p>
      <p>brennockscrapworks.example.co.uk</p>
    </div>
  </section>

  <section class="card card--brand" aria-label="Business card, brand side">
    <div class="wordmark">
      <span class="wordmark__name">brennock</span>
      <span class="wordmark__tagline">Metal Recycling</span>
    </div>
  </section>
</body>
</html>
```